Fun modern label needed for olive oil bottle

I need a label for a boutique handmade olive oil line. It needs to be fun and reflect the smallness of the operation and from rural Australia

The name of the line comes from the fact that I live in rural Australia and the black tar road ends 5 km from my home. The road turns to dusty slippery gravel in summer and wet and slippery gravel mud in winter.
Those of us who live out here say that the best people live WATTLE CREEK HOLLOW.

There are no restrictions on colours but it MUST be fun with clear strong lines.

The label is rectangular with the short sides top and bottom. I shall measure the bottles later today and update the brief for you

Below is an example of the bottles used and there will be 3 different sizes
Updates

I have added a couple of photos to show Australian labels and what is need on them sorry to have left out this crucial information

Industry/Entity Type

Boutique

Requirements
Must have
• Wattle Creek Hollow as name
Some sort of logo

```html
<!DOCTYPE html>
<html lang="en">
<head>
<meta charset="utf-8">
<title>Wattle Creek Hollow – Olive Oil Labels</title>
<link rel="stylesheet" href="https://fonts.googleapis.com/css2?family=Oswald:wght@300;400;500&family=Open+Sans:wght@400;600&family=Pinyon+Script&family=Cormorant+Garamond:wght@500&display=swap">
<style>
  :root {
    --page: #f2f1ee;
    --label-light: #f4f4f4;
    --label-dark: #2b2b2b;
    --ink: #2a2a2a;
    --ink-soft: #5a5a5a;
    --paper-text: #f1f1f1;
    --gold: #c9a227;
    --rule: #8a8a8a;
    --edge: #dcdcdc;
  }
  * { box-sizing: border-box; margin: 0; padding: 0; }
  html, body { width: 1200px; height: 800px; overflow: hidden; }
  body { background: var(--page); position: relative; font-family: "Open Sans", sans-serif; color: var(--ink); }

  .label { position: absolute; border-radius: 6px; overflow: hidden; }
  .label--light { background: var(--label-light); border: 1px solid var(--edge); }
  .label--dark { background: var(--label-dark); color: var(--paper-text); }

  /* Back label */
  .back-label { left: 228px; top: 366px; width: 126px; height: 342px; padding: 10px 8px 8px 9px; }
  .caps { font-family: "Oswald", sans-serif; font-weight: 300; text-transform: uppercase; letter-spacing: .1px; }
  .back-label .heading { font-size: 6.5px; }
  .back-label .body-copy { font-size: 7.5px; line-height: 9.5px; margin-bottom: 9px; }
  .nutrition-title { font-size: 8.5px; font-weight: 300; color: var(--ink-soft); }
  .nutrition-meta { font-size: 5.6px; line-height: 7px; margin-bottom: 9px; }
  .nutrition-table { width: 100%; border-collapse: collapse; font-family: "Oswald", sans-serif; font-weight: 300; font-size: 5.4px; text-transform: uppercase; }
  .nutrition-table td { padding: 0; line-height: 9.6px; white-space: nowrap; }
  .nutrition-table td + td { text-align: center; }
  .company { margin-top: 14px; font-size: 5.6px; line-height: 7px; }
  .company .detail { font-family: "Open Sans", sans-serif; font-size: 6.4px; line-height: 8px; text-transform: none; color: var(--ink-soft); }
  .support { margin-top: 14px; font-size: 5.6px; line-height: 8px; }
  .support strong, .web { font-weight: 500; font-size: 6.4px; }
  .web { margin-top: 16px; }

  /* Front labels */
  .front-label { top: 238px; width: 116px; height: 470px; }
  .front-label--light { left: 541px; }
  .front-label--dark { left: 845px; }
  .brand-mark { position: absolute; left: 25px; top: 12px; width: 66px; height: 66px; }
  .front-label--light .brand-mark { background: var(--ink); }
  .front-label--dark .brand-mark { background: var(--gold); }
  .product-line { position: absolute; left: 25px; top: 83px; font-family: "Oswald", sans-serif; line-height: 10px; }
  .product-line .variety { font-weight: 500; font-size: 8.6px; }
  .product-line .origin { font-weight: 300; font-size: 8.2px; }

  .spine { position: absolute; left: -62px; top: 316px; width: 240px; height: 56px; transform: rotate(-90deg); }
  .spine .brand-name { font-family: "Pinyon Script", cursive; font-size: 30px; line-height: 32px; white-space: nowrap; padding-left: 4px; }
  .spine .tagline-row { display: flex; align-items: center; gap: 7px; margin-top: 2px; }
  .spine .tagline { font-family: "Cormorant Garamond", serif; font-weight: 500; font-size: 11px; letter-spacing: .8px; white-space: nowrap; }
  .double-rule { height: 4px; border-top: 2.5px solid var(--rule); border-bottom: 1px solid var(--rule); flex: none; }
  .double-rule--lead { width: 44px; }
  .double-rule--tail { width: 22px; margin-left: 10px; }
  .front-label--light .spine { color: var(--ink); }
  .front-label--dark .spine { color: var(--paper-text); }
</style>
</head>
<body>

  <section class="label label--light back-label" aria-label="Back label">
    <p class="caps heading">Ingredients:</p>
    <p class="body-copy">100% Australian Extra Virgin Olive Oil.</p>
    <p class="body-copy">Store in a cool dark place away from light and heat.</p>
    <p class="caps nutrition-title">Nutrition Information</p>
    <p class="caps nutrition-meta">Servings per package:<br>60 serving size: 15ml</p>
    <table class="nutrition-table">
      <tr><td>Average quality</td><td>Per 15ml</td><td>Per 100ml</td></tr>
      <tr><td>Energy - kj</td><td>517kj</td><td>3447kj</td></tr>
      <tr><td>Protein</td><td>0.0g</td><td>0.0g</td></tr>
      <tr><td>Fat</td><td></td><td></td></tr>
      <tr><td>-Total</td><td>13.7g</td><td>91.5g</td></tr>
      <tr><td>-Saturated</td><td>2.0g</td><td>13.6g</td></tr>
      <tr><td>-Monounsaturated</td><td>13.7g</td><td>91.5g</td></tr>
      <tr><td>-Polyunsaturated</td><td>1.4g</td><td>9.3g</td></tr>
      <tr><td>-Trans</td><td>&lt;0.01g</td><td>&lt;0.01g</td></tr>
      <tr><td>Cholesterol</td><td>0mg</td><td>0mg</td></tr>
      <tr><td>Carbohydrate</td><td>0mg</td><td>0mg</td></tr>
      <tr><td>-Sugars</td><td>0mg</td><td>0mg</td></tr>
      <tr><td>Sodium</td><td>0.0mg</td><td>0.0mg</td></tr>
    </table>
    <div class="caps company">
      Company information
      <p class="detail">18 Sample Rd<br>Hollow 3714</p>
    </div>
    <p class="caps support">Support and information<br><strong>1-800-WATTLES</strong></p>
    <p class="caps web">www.wattlecreekhollow.com.au</p>
  </section>

  <section class="label label--light front-label front-label--light" aria-label="Front label, light">
    <div class="brand-mark" aria-hidden="true"></div>
    <div class="product-line">
      <p class="variety">EXTRA VIRGIN OLIVE</p>
      <p class="origin">MADE IN AUSTRALIA</p>
    </div>
    <div class="spine">
      <p class="brand-name">Wattle Creek Hollow</p>
      <div class="tagline-row">
        <span class="double-rule double-rule--lead"></span>
        <span class="tagline">BOUTIQUE HANDMADE</span>
        <span class="double-rule double-rule--tail"></span>
      </div>
    </div>
  </section>

  <section class="label label--dark front-label front-label--dark" aria-label="Front label, dark">
    <div class="brand-mark" aria-hidden="true"></div>
    <div class="product-line">
      <p class="variety">EXTRA VIRGIN OLIVE</p>
      <p class="origin">MADE IN AUSTRALIA</p>
    </div>
    <div class="spine">
      <p class="brand-name">Wattle Creek Hollow</p>
      <div class="tagline-row">
        <span class="double-rule double-rule--lead"></span>
        <span class="tagline">BOUTIQUE HANDMADE</span>
        <span class="double-rule double-rule--tail"></span>
      </div>
    </div>
  </section>

</body>
</html>
```